Business card design needed

Family General Practitioner/ Family Physician.
Logo is the logo of the Crestmoor Guild of Family Clinicians Australia
http://kvplm.tarevo.edu.au/PictureGallery/logos/pages/CGFC%20logo_jpg.htm

Reason: Just a bit more time to make changes and the weekend for me to look at things closely and to choose. Thanks, Lumi

Thanks for all the submissions. So many of them are really works of art. Not one of them are not good. The ones that I am eliminating are the ones that I think are not suitable for me personally only, and because if I don't, it makes it very difficult to decide as many of you are also sending me slight variations of a card. I have just decided to choose a second place card too. Can't thank you all enough. Good luck, Lumi. P.S - Working today till 10 pm as the card says :-), so probably won't be able to give a feedback till late Saturday night or Sunday morning here in Sydney, Australia. 

Reason: Just added a second place to the budget and realised that Australia is ahead of the rest of the world in the time zone (only :-) - don't want to offend anyone or start a debate!! ) , so Monday deadline will mean it will be a weekend for the rest of the world. Just wanted to give everyone more time to submit their best, especially since I will be picking a second card too. Can't thank everyone enough for the submissions. P.S - Not keen on photos on the card.

Contact Information for Business Card

Dr. Lumi Harcourt M.B.B.S., F.C.G.F.C
Family General Practitioner
Address, timings, phone and fax number on the back.

Requirements
Must have
• Timings
Mon 7 am - 7 pm
Tues 7 am - 12 pm
Wed 7 am - 10 pm
Thurs 7 am - 12 pm
Fri 7 am - 8 pm
Sat 8 am - 10 pm
Sun - Off

```html
<!DOCTYPE html>
<html lang="en">
<head>
<meta charset="utf-8">
<title>Dr. Lumi Harcourt – Business Card</title>
<link rel="stylesheet" href="https://fonts.googleapis.com/css2?family=Cinzel:wght@400;500&family=Andika&display=swap">
<style>
  :root {
    --page-bg: #8d8d8d;
    --card-white: #ffffff;
    --grad-mauve: #8e6f6c;
    --grad-brown: #3a1f1f;
    --grad-blue: #5b80a6;
    --ink: #2e1f22;
    --ink-soft: #3d3034;
    --accent-blue: #5b8fcc;
    --bar-grey: #b9b9b9;
    --name-white: #f7f3f1;
    --crest-red: #b0262c;
  }
  * { margin: 0; padding: 0; box-sizing: border-box; }
  html, body { width: 1200px; height: 1000px; overflow: hidden; }
  body {
    background: var(--page-bg);
    font-family: "Andika", "Trebuchet MS", sans-serif;
    position: relative;
  }
  .card {
    position: absolute;
    top: 75px;
    width: 490px;
    height: 830px;
    box-shadow: 0 6px 18px rgba(0,0,0,.35);
    overflow: hidden;
  }
  /* Front */
  .card-front {
    left: 80px;
    background: linear-gradient(to bottom,
      var(--card-white) 0%,
      #f2eeee 14%,
      var(--grad-mauve) 36%,
      #5a3a38 50%,
      var(--grad-brown) 64%,
      #4a4a5a 80%,
      var(--grad-blue) 92%,
      var(--grad-blue) 100%);
  }
  .guild-mark {
    position: absolute;
    top: 150px;
    left: 0; right: 0;
    display: flex;
    align-items: center;
    justify-content: center;
    gap: 14px;
  }
  .guild-mark__dot {
    width: 26px; height: 26px;
    border-radius: 50%;
    background: var(--crest-red);
  }
  .guild-mark__name {
    font-family: "Andika", "Trebuchet MS", sans-serif;
    font-size: 40px;
    color: var(--crest-red);
    letter-spacing: 2px;
  }
  .practitioner {
    position: absolute;
    top: 418px;
    left: 0; right: 0;
    text-align: center;
  }
  .practitioner__name {
    font-family: "Cinzel", Georgia, serif;
    font-size: 38px;
    color: var(--name-white);
    letter-spacing: 1px;
    line-height: 1;
  }
  .practitioner__creds {
    margin-top: 12px;
    font-size: 19px;
    color: var(--name-white);
    letter-spacing: 1px;
  }
  .practitioner__role {
    margin-top: 6px;
    font-size: 25px;
    color: var(--accent-blue);
  }
  /* Back */
  .card-back {
    left: 625px;
    background: var(--card-white);
    color: var(--ink);
  }
  .hours__title {
    position: absolute;
    top: 70px; left: 60px;
    font-size: 36px;
    font-weight: 400;
  }
  .hours__list { list-style: none; }
  .hours__row {
    position: absolute;
    left: 50px;
    height: 44px;
    display: flex;
    align-items: baseline;
    font-size: 33px;
    white-space: nowrap;
  }
  .hours__bar {
    position: absolute;
    left: 0; top: 6px;
    height: 34px;
    background: linear-gradient(to right, rgba(185,185,185,.9), var(--bar-grey) 80%, rgba(185,185,185,0));
    filter: blur(3px);
    z-index: 0;
  }
  .hours__day, .hours__time { position: relative; z-index: 1; }
  .hours__day { width: 56px; }
  .hours__time small { font-size: 16px; }
  .hours__off {
    position: absolute;
    top: 450px; left: 55px;
    font-size: 21px;
  }
  .address {
    position: absolute;
    top: 488px; right: 80px;
    text-align: right;
    font-style: normal;
    font-size: 26px;
    line-height: 34px;
    color: var(--accent-blue);
  }
  .contact {
    position: absolute;
    top: 665px; right: 80px;
    text-align: right;
  }
  .contact__tel { font-size: 42px; line-height: 1.1; }
  .contact__fax { font-size: 22px; margin-right: 6px; }
</style>
</head>
<body>

<section class="card card-front" aria-label="Card front">
  <div class="guild-mark">
    <span class="guild-mark__dot"></span>
    <span class="guild-mark__name">CGFC</span>
  </div>
  <div class="practitioner">
    <h1 class="practitioner__name">Dr. Lumi Harcourt</h1>
    <p class="practitioner__creds">M.B.B.S., F.C.G.F.C</p>
    <p class="practitioner__role">Family General Practitioner</p>
  </div>
</section>

<section class="card card-back" aria-label="Card back">
  <h2 class="hours__title">Working hours</h2>
  <ul class="hours__list">
    <li class="hours__row" style="top:140px"><span class="hours__bar" style="width:330px"></span><span class="hours__day">M</span><span class="hours__time">7<small>AM</small>...........7<small>PM</small></span></li>
    <li class="hours__row" style="top:186px"><span class="hours__bar" style="width:230px"></span><span class="hours__day">Tu</span><span class="hours__time">7<small>AM</small>.....12<small>PM</small></span></li>
    <li class="hours__row" style="top:232px"><span class="hours__bar" style="width:400px"></span><span class="hours__day">W</span><span class="hours__time">7<small>AM</small>...................10<small>PM</small></span></li>
    <li class="hours__row" style="top:278px"><span class="hours__bar" style="width:230px"></span><span class="hours__day">Th</span><span class="hours__time">7<small>AM</small>.....12<small>PM</small></span></li>
    <li class="hours__row" style="top:324px"><span class="hours__bar" style="width:350px"></span><span class="hours__day">F</span><span class="hours__time">7<small>AM</small>.............8<small>PM</small></span></li>
    <li class="hours__row" style="top:370px"><span class="hours__bar" style="width:400px"></span><span class="hours__day">Sa</span><span class="hours__time">8<small>AM</small>................10<small>PM</small></span></li>
  </ul>
  <p class="hours__off">Sunday Off</p>
  <address class="address">
    Upper Level<br>
    Arbour Court<br>
    Larkfield Shopping Centre<br>
    Fernleigh Hill<br>
    NSW 2199
  </address>
  <div class="contact">
    <p class="contact__tel">Tel: 02 5550 2400</p>
    <p class="contact__fax">Fax: 025550 2233</p>
  </div>
</section>

</body>
</html>
```